Webdesign für Marke KLARWERK plus
Zielgruppe
R+W Markenwertung besteht seit 1995 und war zunächst jahrzehntelang als klassische Werbeagentur mit den Schwerpunkten Print, VKF und TV tätig. In den vergangenen Jahren hat sich unsere unternehmerische Ausrichtung jedoch zunehmend auf die Bereiche Expansion, Akquisition und Consulting verlagert –hier sind wir schwerpunktmäßig für zwei große deutsche Unternehmen als etablierter Dienstleister tätig.
Aktuell forcieren wir nun unsere Marke KLARWERK plus. Schwerpunkt von KLARWERK plus ist es, das Thema „Hygiene-Auftritt“ künftig zum Bestandteil einer zukunftsorientierten Unternehmensführung bzw. eines erfolgreichen Marketing-Mix zu machen. Zunächst starten wir mit zwei hochwertigen Varianten von wohl einzigartigen Desinfektionsgeräten, die Qualität, Design und eine hohe Marken- Individualisierbarkeit vereinen. Zielgruppe ist der Gesamtbereich B-to-B.
Aufgabenstellung
Aktuell existiert eine erste Broschüre, die aber nicht zwingend das 'Maß der Dinge' sein muss - wir sind da ganz offen! Diese Broschüre fügen wir als pdf bei. Sie ist sehr kurzfristig auf dei beine gestellt worden, vielleicht ist sie auch 'zu un-emotional' und insofern zu wenig zum Kauf anregend. Dann schlagen SIE doch eine andere Art von Website vor!

```html
<!DOCTYPE html>
<html lang="de">
<head>
<meta charset="utf-8">
<title>KLARWERK plus – Unsere Mission</title>
<link href="https://fonts.googleapis.com/css2?family=Montserrat:wght@600;700&family=Poppins:wght@400;500;600&display=swap" rel="stylesheet">
<style>
:root{
  --ink:#14131c;
  --text:#55545c;
  --muted:#a7a7ad;
  --gold:#c8b27c;
  --tile:#f4f4f4;
  --teal-a:#2a9d8b;
  --teal-b:#1d7769;
  --night:#12111a;
  --white:#ffffff;
}
*{margin:0;padding:0;box-sizing:border-box}
html,body{width:1200px;height:2390px;overflow:hidden;background:var(--white)}
body{position:relative;font-family:'Poppins',sans-serif;color:var(--text)}
.abs{position:absolute}
.brand{font-family:'Poppins',sans-serif;font-weight:600;color:var(--ink);letter-spacing:.5px;white-space:nowrap}
.site-header .brand{left:54px;top:14px;font-size:13px}
.main-nav{top:18px;font-size:11px;color:var(--muted);letter-spacing:-.2px}
.main-nav a{position:absolute;color:inherit;text-decoration:none;white-space:nowrap}
.main-nav a.active{color:var(--ink);font-weight:500}
.main-nav .active-mark{position:absolute;top:14px;color:var(--teal-a);font-size:11px}
.plus{position:absolute}
.plus::before,.plus::after{content:"";position:absolute;background:var(--gold)}
.page-title{left:91px;top:145px;font-family:'Montserrat',sans-serif;font-weight:700;font-size:45px;color:var(--ink);letter-spacing:-.5px}
.tile{position:absolute;background:var(--tile);width:266px;height:202px;display:flex;align-items:center;justify-content:center}
.mission h2{position:absolute;font-family:'Montserrat',sans-serif;font-weight:700;font-size:22px;color:var(--ink);letter-spacing:-.3px;white-space:nowrap}
.rule{position:absolute;height:1px;width:50px;background:var(--gold)}
.copy{position:absolute;font-size:11.5px;line-height:17px;color:var(--text)}
.copy p+p{margin-top:17px}
.service-divider{left:1003px;top:936px;width:1px;height:112px;background:#dcdcdc}
.service-label{left:1045px;top:973px;font-size:9.5px;letter-spacing:2px;color:#6d6d73;font-weight:500}
.service-number{left:1045px;top:990px;font-size:13px;color:var(--gold);font-weight:500}
.evolution{left:0;top:1490px;width:813px;height:626px;background:linear-gradient(135deg,var(--teal-a),var(--teal-b))}
.evolution h2{position:absolute;left:118px;top:74px;font-family:'Montserrat',sans-serif;font-weight:700;font-size:22px;line-height:27px;color:var(--white)}
.evolution h3{position:absolute;left:118px;top:194px;font-family:'Montserrat',sans-serif;font-weight:600;font-size:16px;color:var(--white)}
.evolution .copy{left:118px;top:225px;width:500px;color:#e6f3f0}
.cta{position:absolute;left:118px;top:549px;display:flex;align-items:center;gap:28px;font-size:9.5px;letter-spacing:2px;color:var(--white);font-weight:500}
.cta svg{display:block}
.product-visual{left:955px;top:1576px;width:143px;height:417px;border-radius:4px;background:linear-gradient(90deg,#e2e2e4,#fafafa 45%,#cfcfd2)}
.note{left:668px;top:2040px;width:386px;height:127px;background:var(--night);color:#eceaf2;font-size:9px;line-height:14.5px;padding:14px 17px}
.note p+p{margin-top:14px}
.note::before{content:"";position:absolute;right:14px;top:-8px;border-left:9px solid transparent;border-right:9px solid transparent;border-bottom:9px solid var(--night)}
.site-footer .brand{left:56px;top:2272px;font-size:16px}
.copyright{left:50px;top:2347px;font-size:11px;color:var(--ink)}
.footer-col{top:2270px;font-size:9.5px;line-height:19.4px;color:#56555c}
.footer-col h4{font-size:11px;letter-spacing:2.4px;font-weight:500;color:var(--ink);margin-bottom:2px;line-height:16px}
.footer-col a{display:block;color:inherit;text-decoration:none}
</style>
</head>
<body>

<header class="site-header">
  <div class="abs brand">KLARWERK plus</div>
  <nav class="abs main-nav" style="left:0;width:1200px">
    <a style="left:678px">Home</a>
    <a class="active" style="left:760px">Unsere Mission</a>
    <span class="active-mark" style="left:795px">+</span>
    <a style="left:889px">Produkte</a>
    <a style="left:987px">Der Mehrwert</a>
    <a style="left:1107px">Kontakt</a>
  </nav>
</header>

<main>
  <span class="plus" style="left:50px;top:107px;width:40px;height:40px"></span>
  <style>.plus{}.plus::before{left:0;top:50%;width:100%;height:4px;margin-top:-2px}.plus::after{top:0;left:50%;height:100%;width:4px;margin-left:-2px}
  .evolution .plus::before,.evolution .plus::after{background:var(--white)}
  .evolution .plus::before{height:3px;margin-top:-1.5px}.evolution .plus::after{width:3px;margin-left:-1.5px}</style>
  <h1 class="abs page-title">Unsere Mission</h1>

  <section class="mission">
    <div class="tile" style="left:50px;top:286px">
      <svg width="64" height="40" viewBox="0 0 64 40" fill="none" stroke="#14131c" stroke-width="4"><polyline points="2,36 20,18 32,30 58,5"/><polyline points="38,4 60,4 60,26"/></svg>
    </div>
    <h2 style="left:397px;top:298px">Starke Marke</h2>
    <span class="rule" style="left:398px;top:352px"></span>
    <div class="copy" style="left:464px;top:344px;width:560px">
      <p>“KLARWERK plus”: Da weiß jeder sofort, worum es geht. Dieser einprägsame Markenname stellt somit die optimale Basis für eine starke Marke dar, die wir sukzessive entwickeln werden: Sowohl hinsichtlich des inhaltlichen Portfolios an Geräten und Dienstleistungen, als auch im Sinne der gesamten Markenbildung.</p>
      <p>Positiver Nebeneffekt unseres Markennamens: KLARWERK plus ist hinsichtlich seiner Schreibweise international adaptierbar...</p>
    </div>
  </section>

  <section class="mission">
    <h2 style="left:91px;top:599px">Qualität und Design</h2>
    <span class="rule" style="left:92px;top:653px"></span>
    <div class="copy" style="left:158px;top:645px;width:590px">
      <p>Ein Markenname impliziert auch Verantwortung im Sinne hoher Qualität und daher werden die<br>von KLARWERK plus angebotenen Geräte ausschließlich in Deutschland bzw. in Europa gefertigt.</p>
      <p>“Design-orientiert und trotzdem sehr<br>robust” lautet eine weitere Qualitätsmaxime, denn alle unsere Geräte sind  für den harten Dauergebrauch im öffentlichen Raum konzipiert.</p>
    </div>
    <div class="tile" style="left:882px;top:577px">
      <svg width="68" height="68" viewBox="0 0 68 68" fill="none" stroke="#14131c" stroke-width="3.5"><circle cx="34" cy="34" r="31"/><ellipse cx="34" cy="34" rx="13" ry="31"/><line x1="3" y1="34" x2="65" y2="34"/></svg>
    </div>
  </section>

  <section class="mission">
    <div class="tile" style="left:50px;top:868px">
      <svg width="68" height="68" viewBox="0 0 68 68" fill="none" stroke="#14131c" stroke-width="4.5"><path d="M34 3a31 31 0 1 0 0 62h31V34A31 31 0 0 0 34 3z"/><circle cx="22" cy="34" r="1.6" fill="#14131c"/><circle cx="34" cy="34" r="1.6" fill="#14131c"/><circle cx="46" cy="34" r="1.6" fill="#14131c"/></svg>
    </div>
    <h2 style="left:397px;top:890px">Full-Service</h2>
    <span class="rule" style="left:398px;top:944px"></span>
    <div class="copy" style="left:464px;top:936px;width:500px">
      <p>Es versteht sich von selbst, dass  eine unserer Missionen auch ein zuverlässiger Full-Service in allen Bereichen ist: Angefangen mit zuverlässiger Lieferfähigkeit der Hygiene-Stationen, über den schnellen Versand von Verbrauchsmaterialien  bis hin zu telefonischem Support über unsere Servicenummer.</p>
      <p>Ab Anfang 2021 planen wir für die Premium-Station das Angebot eines Mietkaufs.</p>
    </div>
    <div class="abs service-divider"></div>
    <div class="abs service-label">SERVICENUMMER</div>
    <div class="abs service-number">0800 555 0142</div>
  </section>

  <section class="mission">
    <h2 style="left:91px;top:1181px">Individualisierbarkeit</h2>
    <span class="rule" style="left:92px;top:1235px"></span>
    <div class="copy" style="left:158px;top:1227px;width:560px">
      <p>Die Notwendigkeit von Hygiene- Maßnahmen wird auf unabsehbare Zeit bleiben und insofern ist genau jetzt der richtige Zeitpunkt, um den Gesamtbereich der Hygiene zum Teil der Markenstrategie eines Unternehmens zu machen.</p>
      <p>KLARWERK plus bietet hierzu ein umfassendes “Baukastensystem der Individualisierbarkeit”.<br>Viele interessante Details hierzu erfahren Sie auf den folgenden Seiten.</p>
    </div>
    <div class="tile" style="left:882px;top:1159px">
      <svg width="70" height="70" viewBox="0 0 70 70" fill="none" stroke="#14131c" stroke-width="4"><rect x="2" y="2" width="66" height="66" rx="4"/><polyline points="2,50 22,30 44,50"/><polyline points="2,58 68,58"/><circle cx="48" cy="20" r="5"/><polyline points="38,44 50,34 68,48"/></svg>
    </div>
  </section>

  <section class="abs evolution">
    <span class="plus" style="left:93px;top:53px;width:26px;height:26px"></span>
    <h2>Weiterentwicklung steckt<br>in unseren Genen</h2>
    <h3>Neuerfindungen und Portfolioerweiterung</h3>
    <div class="copy">
      <p>Ein “KLARWERK plus-Gedanke” wird auch noch lange nach Corona in den Köpfen und somit in den Verhaltensweisen eines jeden Menschen weltweit verankert bleiben. Grund genug, dass KLARWERK plus als Marke sowohl dem Bereich Produktneuentwicklung als auch der Erweiterung des Produktport-folios hohe Bedeutung beimessen wird.</p>
      <p>Einige Weiterentwicklungen wie z.B. Premium-Säulen mit integrierten, für jeglichen Content nutzbaren Informations-Screens sind bereits ebenso in Arbeit wie die Integration von Fiebermess-Screens.</p>
      <p>Auch im Bereich “Raumlüftung” wird im Jahr 2021 eine Portfolio-Erweiter-ung stattfinden.</p>
      <p>Last but not least: Wir stehen bereits mit einem der renommierten Wissen- schaftler von denen man täglich in der Presse liest in Kontakt, um eine langfristig besonders fachkompetente Ausrichtung der Marke KLARWERK plus zu erreichen.</p>
    </div>
    <div class="cta">PRODUKTE ANSEHEN
      <svg width="24" height="24" viewBox="0 0 24 24" fill="none" stroke="#fff" stroke-width="1"><circle cx="12" cy="12" r="11.5"/><path d="M8 12h8M13 9l3 3-3 3"/></svg>
    </div>
  </section>

  <div class="abs product-visual" role="img" aria-label="Produktfoto einer weißen freistehenden Desinfektionssäule"></div>

  <aside class="abs note">
    <p>So, wie der Homo Sapiens genetisch gesehen nach-gewiesenermaßen noch gar nicht fertig ist, verhält es sich mit zahlreichen technischen Entwicklungen rund um  KLARWERK plus:</p>
    <p>Lassen Sie sich in den nächsten Jahren überraschen, was hier noch alles kommen wird!</p>
  </aside>
</main>

<footer class="site-footer">
  <div class="abs brand">KLARWERK plus</div>
  <div class="abs copyright">© 2020</div>
  <div class="abs footer-col" style="right:297px;text-align:right">
    <h4>NAVIGATION</h4>
    <a>Home</a><a>Unsere Mission</a><a>Produkte</a><a>Der Mehrwert</a>
  </div>
  <div class="abs footer-col" style="left:939px">
    <h4 style="margin-left:8px">KONTAKT</h4>
    <a>Kontaktformular</a>
  </div>
  <div class="abs footer-col" style="right:52px;text-align:right">
    <h4>RECHTLICHES</h4>
    <a>Datenschutz</a><a>AGB</a><a>Impressum</a>
  </div>
</footer>

</body>
</html>
```